Financial Services Business Card Design

We are a financial services company Based in London, offering Short term Funding Solutions for companies, raising anywhere between £20,000 and £25million pounds.

The Card must have a professional look as it is going to be handed out to professionals I.E Solicitors, Accountants, Company directors and Business owners.

See Attached our company Logo

Industry/Entity Type

Business

Contact Information for Business Card

Lewis Thorncroft
Suite 41
R K House
Bramblecote Lane
Watford
HP19 4QX

```html
<!DOCTYPE html>
<html lang="en">
<head>
<meta charset="utf-8">
<title>Meridian Bridge Capital – Business Card</title>
<link rel="stylesheet" href="https://fonts.googleapis.com/css2?family=PT+Sans:wght@400;700&display=swap">
<style>
  :root {
    --backdrop: #3b3430;
    --card: #111111;
    --brand-blue: #2a7fd0;
    --brand-green: #3aa836;
    --ink-light: #e9e9e9;
    --ink-muted: #bdbdbd;
    --rule: #5a5a5a;
  }
  * { box-sizing: border-box; margin: 0; padding: 0; }
  html, body {
    width: 1200px; height: 814px; overflow: hidden;
    background: var(--backdrop);
    font-family: "PT Sans", Arial, sans-serif;
  }
  .canvas {
    position: relative; width: 1200px; height: 814px;
    display: flex; align-items: center; justify-content: center; gap: 48px;
  }
  .card {
    width: 540px; height: 310px;
    background: var(--card);
    border-radius: 4px;
    box-shadow: 0 10px 30px rgba(0,0,0,.45);
    position: relative;
  }
  /* Contact side */
  .card--contact { display: flex; }
  .brand-panel {
    width: 50%;
    display: flex; align-items: center; justify-content: center; gap: 12px;
  }
  .brand-dot {
    width: 16px; height: 16px; border-radius: 50%;
    background: var(--brand-green);
  }
  .brand-name {
    color: var(--brand-blue); font-weight: 700; font-size: 26px;
    line-height: 1.05; letter-spacing: .5px;
  }
  .divider {
    position: absolute; left: 50%; top: 56px; bottom: 56px;
    width: 1px; background: var(--rule);
  }
  .details {
    width: 50%; padding: 66px 0 0 30px;
    color: var(--ink-light); font-size: 15px; line-height: 1.4;
  }
  .details__name {
    color: var(--brand-blue); font-size: 20px; font-weight: 700; margin-bottom: 6px;
  }
  .details__address { margin-bottom: 4px; }
  .contact-line { display: flex; align-items: center; gap: 8px; }
  .contact-line svg { width: 13px; height: 13px; flex: none; }
  /* Front side */
  .card--front {
    display: flex; flex-direction: column; align-items: center; justify-content: center;
  }
  .front-brand { display: flex; align-items: center; gap: 12px; }
  .front-brand .brand-name { font-size: 34px; }
  .front-web {
    margin-top: 26px; color: var(--ink-light);
    font-size: 14px; letter-spacing: 2.5px;
  }
</style>
</head>
<body>
<main class="canvas">
  <section class="card card--contact" aria-label="Contact side">
    <div class="brand-panel">
      <span class="brand-dot"></span>
      <span class="brand-name">Meridian<br>Bridge Capital</span>
    </div>
    <span class="divider"></span>
    <div class="details">
      <p class="details__name">Lewis Thorncroft</p>
      <p class="details__address">Suite 41, R K House<br>Bramblecote Lane, Watford<br>HP19 4QX</p>
      <p class="contact-line">
        <svg viewBox="0 0 16 16"><path fill="#2a7fd0" d="M3.6 1.2l2.3 2.6-1.2 1.9c.9 2 2.5 3.6 4.5 4.5l1.9-1.2 2.6 2.3-1.3 2.4C7.3 13.3 2.7 8.7 1.2 3.6z"/></svg>
        614 528 3907
      </p>
      <p class="contact-line">
        <svg viewBox="0 0 16 16"><rect x="1" y="3" width="14" height="10" fill="#2a7fd0"/><path d="M1 3.5l7 5 7-5" fill="none" stroke="#111" stroke-width="1.4"/></svg>
        hello@meridianbridge.com
      </p>
      <p class="contact-line">
        <svg viewBox="0 0 16 16"><circle cx="8" cy="8" r="7" fill="#2a7fd0"/><path d="M1 8h14M8 1c-3 3-3 11 0 14M8 1c3 3 3 11 0 14" fill="none" stroke="#111" stroke-width="1"/></svg>
        www.meridianbridge.com
      </p>
    </div>
  </section>

  <section class="card card--front" aria-label="Brand side">
    <div class="front-brand">
      <span class="brand-dot"></span>
      <span class="brand-name">Meridian Bridge Capital</span>
    </div>
    <p class="front-web">www.meridianbridge.com</p>
  </section>
</main>
</body>
</html>
```